business card

Business card for new business.
Red and black corporate colors.
Card can have an Indsutrial feel to it. Feel free to add Rust, Bolted steel, or graphics as you see fit. We provide highly specialized services to the below mentioned industries.
Keep information out of corners so that if I want I can choose rounded corners.
Information
- front. name - title - phone - email
- Rear
Pipelines - Port - Construction - Forestry - Utilities
Ridgeford - Ashcombe - Port Halvern - Stonebrook - Westmere

```html
<!DOCTYPE html>
<html lang="en">
<head>
<meta charset="utf-8">
<title>Girderline Business Card</title>
<link rel="stylesheet" href="https://fonts.googleapis.com/css2?family=Roboto+Condensed:wght@700&family=Source+Sans+3:wght@400;700;900&display=swap">
<style>
  :root {
    --backdrop: #2a2a2b;
    --card: #1f2022;
    --red: #e3101b;
    --red-deep: #8a0a10;
    --white: #f2f2f2;
    --muted: #d9d9d9;
    --rule: #8c8c8c;
  }
  * { margin: 0; padding: 0; box-sizing: border-box; }
  html, body {
    width: 1200px; height: 960px; overflow: hidden;
    background: var(--backdrop);
    font-family: "Source Sans 3", "Myriad Pro", sans-serif;
  }
  .card {
    position: absolute;
    width: 600px; height: 342px;
    background: var(--card);
  }
  .card-front { left: 303px; top: 125px; }
  .card-back { left: 299px; top: 493px; }

  .frame {
    position: absolute;
    left: 17px; top: 16px; width: 564px; height: 308px;
    border: 3px solid transparent;
    border-image: linear-gradient(135deg, var(--red) 0%, var(--red) 55%, var(--red-deep) 85%, #000 100%) 1;
  }

  .identity {
    position: absolute;
    right: 327px; top: 144px;
    text-align: right;
  }
  .person-name {
    font-family: "Roboto Condensed", "Arial Narrow", sans-serif;
    font-weight: 700;
    font-size: 31px;
    line-height: 32px;
    color: var(--red);
    letter-spacing: 0.2px;
  }
  .person-title {
    font-size: 15.5px;
    line-height: 18px;
    color: var(--muted);
  }
  .divider {
    position: absolute;
    left: 297px; top: 140px;
    width: 1px; height: 60px;
    background: var(--rule);
  }
  .contact-list {
    position: absolute;
    left: 324px; top: 141px;
    list-style: none;
  }
  .contact-list li {
    display: flex; align-items: center;
    height: 19.5px;
    font-size: 15px;
    color: var(--white);
  }
  .contact-list svg { width: 13px; height: 13px; margin-right: 8px; fill: var(--red); }

  .brand {
    position: absolute;
    left: 0; right: 0; top: 140px;
    display: flex; justify-content: center; align-items: center; gap: 12px;
  }
  .brand-mark { width: 18px; height: 18px; background: var(--red); }
  .brand-name {
    font-weight: 900;
    font-size: 46px;
    line-height: 50px;
    letter-spacing: 1px;
    color: var(--white);
    text-transform: uppercase;
  }
  .services {
    position: absolute;
    left: 0; right: 0; top: 256px;
    text-align: center;
    font-size: 15.5px;
    line-height: 19.5px;
    color: var(--white);
  }
  .sep { color: var(--red); font-size: 10px; vertical-align: 2px; margin: 0 2px; }
</style>
</head>
<body>

<section class="card card-front" aria-label="Card front">
  <div class="frame"></div>
  <div class="identity">
    <div class="person-name">MARK DALEN</div>
    <div class="person-title">PRESIDENT</div>
  </div>
  <div class="divider"></div>
  <ul class="contact-list">
    <li>
      <svg viewBox="0 0 16 16" aria-hidden="true"><path d="M1 6c0-3 3-4 7-4s7 1 7 4v1h-4V5H5v2H1zM4 8h8l2 6H2z"/></svg>
      555 0142 7780
    </li>
    <li>
      <svg viewBox="0 0 16 16" aria-hidden="true"><path d="M1 3h14v10H1z M1 3l7 6 7-6" stroke="#1f2022" stroke-width="1.2"/></svg>
      mark@girderline.com
    </li>
    <li>
      <svg viewBox="0 0 16 16" aria-hidden="true"><circle cx="8" cy="8" r="7"/><path d="M4 5h4l1 3-3 1 1 4M10 3l2 3" stroke="#1f2022" stroke-width="1.3" fill="none"/></svg>
      www.girderline.com
    </li>
  </ul>
</section>

<section class="card card-back" aria-label="Card back">
  <div class="brand">
    <span class="brand-mark"></span>
    <span class="brand-name">Girderline</span>
  </div>
  <p class="services">
    Pipelines <span class="sep">●</span> Port <span class="sep">●</span> Construction <span class="sep">●</span> Forestry<br>
    Utilities <span class="sep">●</span> Ridgeford <span class="sep">●</span> Ashcombe <span class="sep">●</span> Port Halvern<br>
    Stonebrook <span class="sep">●</span> Westmere
  </p>
</section>

</body>
</html>
```